Tradeshow Banner Design (Qty2, 6'H x 2'W)

Keystone Works is an Electrical, Fire Alarm, and Security Contracting company. For tradeshows, we would like 2 vertical Banners to put behind our booth. Our colors are Red, Grey & Black. I would like the Banners to be informative on what services we provide, with some appealing Graphic Design. (kwb-plq.com)
Slogan: Safeguarding Communities Electrical, Fire & Security Solutions
Target Market(s)
Commercial Construction Clients
Industry/Entity Type
Electrical / Construction
Font styles to use
Other font styles liked:
- Aileron
Colors
EB3D1F
EC4F4E
F09395
F8D3D4
FCEDEE
Requirements
Must have
- Our Logo, Color Scheme, Brief Caption of the services we provide
Nice to have
- Appealing Imagery & a modern/simplistic design

```html
<!DOCTYPE html>
<html lang="en">
<head>
<meta charset="utf-8">
<title>Keystone Works – Tradeshow Banners</title>
<link href="https://fonts.googleapis.com/css2?family=Bebas+Neue&family=Roboto:wght@400;500&display=swap" rel="stylesheet">
<style>
  :root{
    --page:#ececec;
    --red-deep:#a51c22;
    --red:#e8202a;
    --red-bright:#ed2a33;
    --sky:#4a86cf;
    --night:#1c2a33;
    --white:#ffffff;
    --ink:#111111;
    --head:"Bebas Neue", sans-serif;
    --body:"Roboto", sans-serif;
  }
  *{box-sizing:border-box;margin:0;padding:0}
  html,body{width:1200px;height:994px;overflow:hidden;background:var(--page)}
  .stage{position:relative;width:1200px;height:994px}
  .banner{position:absolute;top:100px;width:248px;height:744px;overflow:hidden;color:var(--white);font-family:var(--body)}
  .banner--one{left:139px}
  .banner--two{left:489px}
  .banner--three{left:849px}
  .caption{position:absolute;top:880px;width:248px;text-align:center;font-family:var(--body);font-size:20px;font-weight:500;color:var(--ink)}
  .headline{position:absolute;left:0;right:0;text-align:center;font-family:var(--head);line-height:.86;letter-spacing:.5px}
  .headline span{display:block}
  .tagline{position:absolute;left:0;right:0;text-align:center;line-height:1.18}
  .services{position:absolute;display:flex;justify-content:center;left:10px;right:10px}
  .service{flex:1;display:flex;flex-direction:column;align-items:center;justify-content:flex-start;text-align:center;border-right:1px solid rgba(255,255,255,.35);line-height:1.1}
  .service:last-child{border-right:none}
  .service svg{fill:var(--white)}
  .brand{position:absolute;left:0;right:0;display:flex;align-items:center;justify-content:center;gap:6px;font-family:var(--head);letter-spacing:.5px}
  .brand-dot{border-radius:50%;background:var(--white);flex:none}
  .web{position:absolute;left:0;right:0;text-align:center;font-weight:500}
  .photo{position:absolute;left:0;right:0}

  /* Version 1 */
  .banner--one{background:var(--night)}
  .banner--one .photo{top:250px;bottom:0;background:linear-gradient(180deg,var(--sky) 0%,#3d6fae 28%,#2f4a66 45%,#3d4b3a 62%,#2b4a2e 78%,#18262c 100%)}
  .banner--one .top-band{position:absolute;top:0;left:0}
  .banner--one .headline{top:70px}
  .banner--one .tagline{top:318px;font-size:12.5px}
  .banner--one .services{top:362px}
  .banner--one .service{font-size:8px;height:55px}
  .banner--one .brand{top:630px;font-size:22px}
  .banner--one .web{top:684px;font-size:16px}

  /* Version 2 */
  .banner--two{background:linear-gradient(180deg,var(--red-deep) 0%,var(--red) 30%,var(--red-bright) 70%,#c41d26 100%)}
  .banner--two .headline{top:64px}
  .banner--two .tagline{top:226px;font-size:13px}
  .banner--two .services{top:266px}
  .banner--two .service{font-size:7.5px;height:48px}
  .banner--two .photo{top:336px;height:244px;background:linear-gradient(120deg,#4b5058 0%,#7a7f86 40%,#5d6168 70%,#2f3236 100%)}
  .banner--two .brand{top:625px;font-size:21px}
  .banner--two .web{top:666px;font-size:16px}

  /* Version 3 */
  .banner--three{background:var(--night)}
  .banner--three .photo{top:0;bottom:0;background:linear-gradient(180deg,var(--red-deep) 0%,var(--red) 25%,#d81f28 45%,#8e2a22 62%,#4a3a2c 74%,#2a3a28 86%,#121c20 100%)}
  .banner--three .headline{top:52px}
  .banner--three .tagline{top:226px;font-size:16px}
  .banner--three .grid{position:absolute;top:268px;left:22px;right:22px;display:grid;grid-template-columns:1fr 1fr}
  .banner--three .service{font-size:12px;height:84px;padding-top:4px;border-right:1px solid rgba(255,255,255,.3);border-bottom:1px solid rgba(255,255,255,.3)}
  .banner--three .service:nth-child(2n){border-right:none}
  .banner--three .service:nth-child(n+3){border-bottom:none;padding-top:10px}
  .banner--three .brand{top:620px;font-size:30px;gap:8px}
  .banner--three .web{top:680px;font-size:16px}
</style>
</head>
<body>
<svg width="0" height="0" style="position:absolute" aria-hidden="true">
  <symbol id="icon-alarm" viewBox="0 0 24 24"><path d="M12 2a2 2 0 0 1 2 2v.6A7 7 0 0 1 19 11v5l2 2v1H3v-1l2-2v-5a7 7 0 0 1 5-6.4V4a2 2 0 0 1 2-2zm-2.5 18h5a2.5 2.5 0 0 1-5 0z"/></symbol>
  <symbol id="icon-bolt" viewBox="0 0 24 24"><path d="M14 1 5 14h6l-2 9 10-14h-6z"/></symbol>
  <symbol id="icon-camera" viewBox="0 0 24 24"><path d="M6 5l15 5-2 5-15-5zM9 13l3 1-1 3H7v3H4v-8h3v3h1z"/></symbol>
  <symbol id="icon-shield" viewBox="0 0 24 24"><path d="M12 1 3 4v7c0 6 4 10 9 12 5-2 9-6 9-12V4zm0 2.2 7 2.3V11c0 4.8-3 8-7 9.8C8 19 5 15.8 5 11V5.5z"/><path d="M7.5 11.5l3 3 6-6 1.4 1.4-7.4 7.4-4.4-4.4z"/></symbol>
</svg>

<main class="stage">

  <section class="banner banner--one">
    <div class="photo" role="img" aria-label="Photo of a modern apartment complex with lit gardens at dusk"></div>
    <svg class="top-band" width="248" height="320" viewBox="0 0 248 320" aria-hidden="true">
      <defs><linearGradient id="redOne" x1="0" y1="0" x2="0" y2="1"><stop offset="0" stop-color="#a51c22"/><stop offset=".6" stop-color="#e8202a"/><stop offset="1" stop-color="#ed2a33"/></linearGradient></defs>
      <path d="M0 0H248V260Q120 290 0 310Z" fill="url(#redOne)"/>
    </svg>
    <h1 class="headline">
      <span style="font-size:112px">SAFE</span>
      <span style="font-size:56px">GUARDING</span>
      <span style="font-size:43px">COMMUNITIES</span>
    </h1>
    <p class="tagline">We help our clients<br>get peace of mind in:</p>
    <ul class="services">
      <li class="service"><svg width="24" height="26"><use href="#icon-alarm"/></svg><span style="margin-top:6px">Fire<br>Protection</span></li>
      <li class="service"><svg width="24" height="26"><use href="#icon-bolt"/></svg><span style="margin-top:6px">Electrical<br>Services</span></li>
      <li class="service"><svg width="32" height="28"><use href="#icon-camera"/></svg><span style="margin-top:12px">Surveillance</span></li>
      <li class="service"><svg width="26" height="28"><use href="#icon-shield"/></svg><span style="margin-top:12px">Security</span></li>
    </ul>
    <div class="brand"><span class="brand-dot" style="width:40px;height:40px"></span><span>KEYSTONE WORKS</span></div>
    <p class="web">www.kwb-plq.com</p>
  </section>

  <section class="banner banner--two">
    <h1 class="headline">
      <span style="font-size:66px">SAFE</span>
      <span style="font-size:50px">GUARDING</span>
      <span style="font-size:40px">COMMUNITIES</span>
    </h1>
    <p class="tagline">We help our clients<br>get peace of mind in:</p>
    <ul class="services">
      <li class="service"><svg width="20" height="24"><use href="#icon-alarm"/></svg><span style="margin-top:4px">Fire<br>Protection</span></li>
      <li class="service"><svg width="20" height="24"><use href="#icon-bolt"/></svg><span style="margin-top:4px">Electrical<br>Services</span></li>
      <li class="service"><svg width="28" height="26"><use href="#icon-camera"/></svg><span style="margin-top:10px">Surveillance</span></li>
      <li class="service"><svg width="24" height="26"><use href="#icon-shield"/></svg><span style="margin-top:10px">Security</span></li>
    </ul>
    <div class="photo" role="img" aria-label="Photo of an electrician in hard hat and safety glasses working on a wiring panel"></div>
    <div class="brand"><span class="brand-dot" style="width:38px;height:38px"></span><span>KEYSTONE WORKS</span></div>
    <p class="web">www.kwb-plq.com</p>
  </section>

  <section class="banner banner--three">
    <div class="photo" role="img" aria-label="Red gradient fading into a photo of a modern apartment complex at dusk"></div>
    <h1 class="headline">
      <span style="font-size:104px">SAFE</span>
      <span style="font-size:52px">GUARDING</span>
      <span style="font-size:40px">COMMUNITIES</span>
    </h1>
    <p class="tagline">We help our client<br>get peace of mind</p>
    <ul class="grid">
      <li class="service"><svg width="30" height="40"><use href="#icon-alarm"/></svg><span style="margin-top:6px">Fire<br>Protection</span></li>
      <li class="service"><svg width="30" height="40"><use href="#icon-bolt"/></svg><span style="margin-top:6px">Electrical<br>Services</span></li>
      <li class="service"><svg width="44" height="40"><use href="#icon-camera"/></svg><span style="margin-top:8px">Surveillance</span></li>
      <li class="service"><svg width="36" height="40"><use href="#icon-shield"/></svg><span style="margin-top:8px">Security</span></li>
    </ul>
    <div class="brand"><span class="brand-dot" style="width:56px;height:56px"></span><span>KEYSTONE WORKS</span></div>
    <p class="web">www.kwb-plq.com</p>
  </section>

  <p class="caption" style="left:139px">Version 1</p>
  <p class="caption" style="left:489px">Version 2</p>
  <p class="caption" style="left:849px">Version 3</p>
</main>
</body>
</html>
```